Design for social media advertising campaign

Multiple designs to be produced for a legal services advertising campaign in Australia offering assistance to small to medium sized businesses facing financial issues arising from the economic consequences of Covid-19. Designs must be sized suitably for LinkedIn, Twitter and Facebook. See our website recovery.harbourline.example and Facebook page QuillardLaw.CoastAdvisers for logo, colours etc. Examples of the messaging is in the 5 uploaded files.

Target Market(s)

Small / medium size business owners

Industry/Entity Type

Legal

Requirements
Must have
• Sizing for Facebook, LinkedIn and Twitter

```html
<!DOCTYPE html>
<html lang="en">
<head>
<meta charset="utf-8">
<title>Business Solvency Campaign – Social Banners</title>
<link rel="stylesheet" href="https://fonts.googleapis.com/css2?family=Jost:ital,wght@0,300;0,500;1,500&family=Roboto+Condensed:wght@700&family=Roboto:wght@700&display=swap">
<style>
  :root {
    --gold: #d4af37;
    --crimson: #7a0020;
    --crimson-deep: #6a001b;
    --paper: #ffffff;
    --desk: #eef0f2;
    --chair: #e6dcc0;
    --window: #c9d3d8;
  }
  * { margin: 0; padding: 0; box-sizing: border-box; }
  html, body { width: 953px; height: 1200px; overflow: hidden; }
  body { position: relative; background: var(--crimson); }

  .backdrop { position: absolute; inset: 0; }

  .banner {
    position: absolute;
    left: 56px;
    width: 840px;
    height: 504px;
    background: var(--paper);
    overflow: hidden;
    box-shadow: 0 0 40px rgba(0,0,0,0.35);
  }
  .banner--top { top: 48px; }
  .banner--bottom { top: 627px; }

  .banner__photo {
    position: absolute;
    inset: 0;
    background:
      radial-gradient(ellipse 150px 210px at 595px 300px, rgba(210,190,175,0.55), rgba(210,190,175,0) 100%),
      radial-gradient(ellipse 120px 260px at 770px 300px, rgba(230,220,192,0.9), rgba(230,220,192,0) 100%),
      linear-gradient(90deg, rgba(255,255,255,1) 0%, rgba(255,255,255,1) 40%, rgba(238,242,245,1) 62%, var(--window) 85%, #e9eef1 100%);
  }
  .banner__photo::after {
    content: "";
    position: absolute;
    left: 0; right: 0; bottom: 0;
    height: 70px;
    background: linear-gradient(180deg, rgba(255,255,255,0), var(--desk));
  }

  .banner__copy {
    position: absolute;
    left: 75px;
    top: 0;
    color: var(--crimson);
  }
  .headline__lead {
    position: absolute;
    top: 72px;
    font-family: "Jost", sans-serif;
    font-weight: 500;
    font-size: 45px;
    line-height: 1;
    white-space: nowrap;
  }
  .headline__main {
    position: absolute;
    top: 114px;
    font-family: "Roboto Condensed", sans-serif;
    font-weight: 700;
    font-size: 88px;
    line-height: 72px;
    letter-spacing: -0.5px;
    white-space: nowrap;
    transform: scaleX(1.02);
    transform-origin: left;
  }
  .headline__tail {
    position: absolute;
    top: 270px;
    font-family: "Jost", sans-serif;
    font-weight: 300;
    font-size: 53px;
    line-height: 1;
    letter-spacing: 5px;
    white-space: nowrap;
  }
  .offer {
    position: absolute;
    top: 350px;
    font-family: "Jost", sans-serif;
    font-style: italic;
    font-weight: 500;
    font-size: 22px;
    letter-spacing: 1.3px;
    white-space: nowrap;
  }
  .firm {
    position: absolute;
    top: 410px;
    left: -2px;
    font-family: "Roboto", sans-serif;
    font-weight: 700;
    font-size: 21px;
    white-space: nowrap;
  }

  .banner--top .headline__lead,
  .banner--top .headline__tail,
  .banner--top .firm { color: var(--crimson); }
  .banner--top .headline__main,
  .banner--top .offer { color: var(--gold); }

  .banner--bottom .headline__lead,
  .banner--bottom .headline__tail,
  .banner--bottom .firm { color: var(--gold); }
  .banner--bottom .headline__main,
  .banner--bottom .offer { color: var(--crimson); }
</style>
</head>
<body>
  <svg class="backdrop" width="953" height="1200" viewBox="0 0 953 1200" aria-hidden="true">
    <rect width="953" height="1200" fill="var(--crimson)"/>
    <polygon points="0,0 953,0 953,385 0,562" fill="var(--gold)"/>
  </svg>

  <section class="banner banner--top">
    <div class="banner__photo" role="img" aria-label="Photo of a stressed business owner at a desk with a laptop, holding her head, bright office window behind"></div>
    <div class="banner__copy">
      <p class="headline__lead">Facing</p>
      <h1 class="headline__main">BUSINESS<br>SOLVENCY</h1>
      <p class="headline__tail">ISSUES?</p>
      <p class="offer">Obtain Our Free Guide NOW</p>
      <p class="firm">HARBOURLINE RECOVERY LAWYERS</p>
    </div>
  </section>

  <section class="banner banner--bottom">
    <div class="banner__photo" role="img" aria-label="Photo of a stressed business owner at a desk with a laptop, holding her head, bright office window behind"></div>
    <div class="banner__copy">
      <p class="headline__lead">Facing</p>
      <h1 class="headline__main">BUSINESS<br>SOLVENCY</h1>
      <p class="headline__tail">ISSUES?</p>
      <p class="offer">Obtain Our Free Guide NOW</p>
      <p class="firm">HARBOURLINE RECOVERY LAWYERS</p>
    </div>
  </section>
</body>
</html>
```